Harbour Stone Advisory Double Sided DL Flyer

We need a double sided flyer that we provide to a Real Estate agent for leeds. It should provide our basic services as well as a modern look and feel. The brochure should incorporate our Brand colors and have a graphic that centres around money and property. I have included a couple of pictures that we like (but have not yet purchased from PIXVAULT) as an indication of the type of picture we like.

WE need to also show the Harbour Stone Advisory brand and have our Phone / address's and email details.

Target Market(s)

Realestate clients (Property Investors)

Industry/Entity Type

Financial Planning

Requirements
Must have
• Picture on Front (maybe the logo on back)
• Please incorporate existing logo colours.

```html
<!DOCTYPE html>
<html lang="en">
<head>
<meta charset="utf-8">
<title>Harbour Stone Advisory – DL Flyer</title>
<link rel="stylesheet" href="https://fonts.googleapis.com/css2?family=Open+Sans:wght@300;400;600;700;800&display=swap">
<style>
  :root {
    --brand-green: #8cc63f;
    --brand-green-deep: #6fae24;
    --ink: #1a1a1a;
    --paper: #ffffff;
    --stage: #e4ddd2;
    --photo-dark: #2f6a1c;
    --photo-mid: #5d9a2e;
    --photo-light: #b9d98a;
    --coin: #b98c52;
  }
  * { box-sizing: border-box; margin: 0; padding: 0; }
  html, body { width: 1200px; height: 1170px; overflow: hidden; }
  body {
    background: var(--stage);
    font-family: "Open Sans", Arial, sans-serif;
    position: relative;
  }
  .flyer {
    position: absolute;
    left: 60px;
    width: 1080px;
    height: 512px;
    overflow: hidden;
    box-shadow: 0 6px 18px rgba(0,0,0,0.18);
  }
  .flyer--front { top: 48px; }
  .flyer--back { top: 610px; background: var(--brand-green); }

  /* Front */
  .front-photo {
    position: absolute; inset: 0;
    background:
      radial-gradient(ellipse 40% 45% at 78% 8%, rgba(240,250,200,0.85), transparent 70%),
      radial-gradient(ellipse 30% 35% at 55% 78%, rgba(205,160,100,0.75), transparent 70%),
      radial-gradient(ellipse 22% 30% at 22% 80%, rgba(210,160,100,0.8), transparent 70%),
      linear-gradient(160deg, var(--photo-mid) 0%, var(--photo-dark) 45%, var(--photo-mid) 75%, var(--photo-light) 100%);
  }
  .headline {
    position: absolute; left: 0; top: 0;
    color: var(--paper);
    font-weight: 700;
    text-shadow: 0 2px 6px rgba(0,0,0,0.35);
    line-height: 1;
  }
  .headline span { position: absolute; white-space: nowrap; }
  .hl-build   { left: 177px; top: 18px;  font-size: 46px; }
  .hl-your1   { left: 143px; top: 52px;  font-size: 38px; color: #dfe9d2; }
  .hl-business{ left: 96px;  top: 66px;  font-size: 80px; }
  .hl-amp     { left: 462px; top: 104px; font-size: 34px; font-weight: 400; color: #dfe9d2; }
  .hl-grow    { left: 466px; top: 134px; font-size: 44px; }
  .hl-your2   { left: 418px; top: 172px; font-size: 38px; color: #dfe9d2; }
  .hl-wealth  { left: 342px; top: 186px; font-size: 82px; }
  .web-bar {
    position: absolute; right: 0; bottom: 0;
    width: 456px; height: 50px;
    background: var(--brand-green);
    color: var(--paper);
    font-weight: 700; font-size: 24px;
    display: flex; align-items: center; justify-content: flex-end;
    padding-right: 18px;
  }

  /* Back */
  .back-header { position: absolute; inset: 0; }
  .brand {
    position: absolute; left: 22px; top: 30px;
  }
  .brand-row { display: flex; align-items: center; gap: 16px; }
  .brand-mark { width: 52px; height: 52px; background: var(--brand-green); }
  .brand-name {
    font-weight: 800; font-size: 44px; color: var(--ink);
    letter-spacing: -0.5px; line-height: 1;
  }
  .brand-tagline {
    margin-top: 18px;
    font-weight: 700; font-size: 14px; color: var(--ink);
    letter-spacing: 0.3px;
  }
  .back-photo {
    position: absolute; left: 13px; top: 194px;
    width: 413px; height: 201px;
    border: 3px solid rgba(255,255,255,0.6);
    background:
      radial-gradient(ellipse 18% 30% at 78% 55%, rgba(230,230,220,0.9), transparent 70%),
      radial-gradient(ellipse 35% 25% at 40% 88%, rgba(185,140,82,0.85), transparent 70%),
      linear-gradient(135deg, #9cc45a 0%, #6e9c34 45%, #b6d27a 80%, #e6d69a 100%);
  }
  .services {
    position: absolute; left: 477px; top: 198px;
    color: var(--paper);
  }
  .services-title {
    color: var(--ink);
    font-weight: 700; font-size: 27px; line-height: 1.0;
  }
  .services-list { list-style: none; margin-top: 6px; }
  .services-list li {
    font-size: 20px; font-weight: 600; line-height: 31px;
    position: relative; padding-left: 30px;
  }
  .services-list li::before {
    content: ""; position: absolute; left: 0; top: 13px;
    width: 7px; height: 7px; border-radius: 50%; background: var(--ink);
  }
  .services-list li:nth-child(1) { margin-left: 62px; }
  .services-list li:nth-child(2) { margin-left: 70px; }
  .services-list li:nth-child(3) { margin-left: 78px; }
  .services-list li:nth-child(4) { margin-left: 86px; }
  .services-list li:nth-child(5) { margin-left: 94px; }
  .contact-bar {
    position: absolute; left: 0; right: 0; bottom: 0; height: 99px;
    background: var(--ink);
    color: var(--paper);
    padding: 6px 0 0 16px;
  }
  .contact-name { font-weight: 300; font-size: 22px; line-height: 1.25; }
  .contact-address { font-weight: 700; font-size: 17px; line-height: 1.45; }
  .contact-note { color: var(--brand-green); font-weight: 600; }
  .contact-phone {
    position: absolute; right: 50px; top: 18px;
    color: var(--brand-green);
    font-weight: 700; font-size: 56px; line-height: 1;
  }
</style>
</head>
<body>

<section class="flyer flyer--front" aria-label="Flyer front">
  <div class="front-photo" role="img" aria-label="Photo of a small wooden house beside rising stacks of gold coins with seedlings sprouting on top, against a soft green garden background"></div>
  <h1 class="headline">
    <span class="hl-build">Build</span>
    <span class="hl-your1">Your</span>
    <span class="hl-business">Business</span>
    <span class="hl-amp">&amp;</span>
    <span class="hl-grow">Grow</span>
    <span class="hl-your2">Your</span>
    <span class="hl-wealth">Wealth</span>
  </h1>
  <div class="web-bar">www.harbourstoneadvisory.com.au</div>
</section>

<section class="flyer flyer--back" aria-label="Flyer back">
  <svg class="back-header" width="1080" height="512" viewBox="0 0 1080 512" aria-hidden="true">
    <defs>
      <filter id="header-shadow" x="-5%" y="-5%" width="110%" height="130%">
        <feDropShadow dx="2" dy="3" stdDeviation="3" flood-color="#000" flood-opacity="0.25"/>
      </filter>
    </defs>
    <polygon points="0,0 1080,0 1080,60 653,60 715,182 0,182" fill="#ffffff" filter="url(#header-shadow)"/>
  </svg>

  <div class="brand">
    <div class="brand-row">
      <span class="brand-mark"></span>
      <span class="brand-name">Harbour Stone Advisory</span>
    </div>
    <div class="brand-tagline">BUILD YOUR BUSINESS &amp; GROW YOUR WEALTH</div>
  </div>

  <div class="back-photo" role="img" aria-label="Photo of coin stacks of increasing height with seedlings, next to a glass jar full of coins, on a blurred green background"></div>

  <div class="services">
    <h2 class="services-title">Accountants and Financial Advisors<br>who specialise in:</h2>
    <ul class="services-list">
      <li>Negative Gearing &amp; Investment Properties</li>
      <li>Property &amp; Capital Gains Tax Minimisation</li>
      <li>Self-Managed Superannuation Funds (SMSF)</li>
      <li>Small Business &amp; Personal Taxation</li>
      <li>Investment Advice &amp; Risk Insurances</li>
    </ul>
  </div>

  <div class="contact-bar">
    <div class="contact-name">Leon Marsh</div>
    <div class="contact-address">4 / 118 Bayview Rd Kelso Bay NSW 2251</div>
    <div class="contact-address">2 / 37 Marina Pde Linden Point NSW 2264 <span class="contact-note">(By Appointment)</span></div>
    <div class="contact-phone">(02) 40001234</div>
  </div>
</section>

</body>
</html>
```